Looking for updated Letterhead and Compliments Slips to go with our new updated logo. This stationary will be used for letters to suppliers and customers so needs to be practical while also quite classic.

We are an engineering company so needs to be clean and precise

Target Market(s)

SME'S and large automotive customers

Industry/Entity Type

Automotive

Font styles to use
Sans Serif

Colors
85acd3
0356a4
0792cd
33a6d7
85abd2
ffffff

Requirements
Must have
• Address details as below
• KT Fabrications Limited
• Hallmere Road
• Dunmore
• Elmshire
• LP47 9XZ, UK
• Telephone: +44 (0)1632 960418
• Fax: +44 (0)1632 960733
• Email: sales@ktfabrications.example
• Web: www.ktfabrications.example
Nice to have
• Nice to have some element of being a British Manufacturer

```html
<!DOCTYPE html>
<html lang="en">
<head>
<meta charset="utf-8">
<title>KT Fabrications – Letterhead and Compliments Slip</title>
<link rel="stylesheet" href="https://fonts.googleapis.com/css2?family=Montserrat:wght@500&family=Source+Sans+3:wght@400&display=swap">
<style>
  :root {
    --backdrop: #d6d6d6;
    --paper: #ffffff;
    --brand-blue: #0356a4;
    --ink: #1c1c1c;
    --rule: #0356a4;
    --hairline: #e2e2e2;
  }
  * { margin: 0; padding: 0; box-sizing: border-box; }
  html, body {
    width: 1200px; height: 1200px; overflow: hidden;
    background: var(--backdrop);
  }
  .canvas { position: relative; width: 1200px; height: 1200px; }

  .sheet { position: absolute; background: var(--paper); }

  .letterhead { left: 22px; top: 56px; width: 668px; height: 946px; }
  .comp-slip  { left: 621px; top: 586px; width: 565px; height: 252px; border: 1px solid var(--hairline); }

  .brand-name {
    position: absolute;
    font-family: "Montserrat", sans-serif;
    font-weight: 500;
    color: var(--brand-blue);
    letter-spacing: 0.32em;
    white-space: nowrap;
  }
  .letterhead .brand-name {
    left: 0; right: 0; top: 120px; text-align: center;
    font-size: 22px; padding-left: 0.32em;
  }
  .comp-slip .brand-name { left: 25px; top: 64px; font-size: 11px; }

  .slip-title {
    position: absolute; right: 33px; top: 54px;
    font-family: "Source Sans 3", sans-serif;
    font-weight: 400;
    font-size: 19px; color: var(--brand-blue);
  }

  .contact-footer {
    position: absolute;
    font-family: "Source Sans 3", sans-serif;
    color: var(--ink);
    display: flex; align-items: center;
    white-space: nowrap;
  }
  .letterhead .contact-footer { left: 48px; top: 874px; font-size: 13px; line-height: 16.5px; }
  .comp-slip .contact-footer  { left: 25px; top: 200px; font-size: 10px; line-height: 12.5px; }

  .contact-address { font-style: normal; }
  .contact-block { padding-right: 20px; }
  .contact-rule { width: 3px; background: var(--rule); margin-right: 16px; }
  .letterhead .contact-rule { height: 38px; }
  .comp-slip .contact-rule { height: 28px; width: 2px; margin-right: 14px; }
  .comp-slip .contact-block { padding-right: 14px; }

  .contact-line { display: flex; align-items: center; gap: 12px; margin: 2px 0; }
  .comp-slip .contact-line { gap: 10px; }
  .icon { width: 12px; height: 12px; flex: none; fill: var(--brand-blue); }
  .comp-slip .icon { width: 9px; height: 9px; }
</style>
</head>
<body>
<div class="canvas">

  <section class="sheet letterhead" aria-label="Letterhead">
    <div class="brand-name">KT FABRICATIONS</div>

    <footer class="contact-footer">
      <address class="contact-block contact-address">
        KT Fabrications Limited<br>
        Hallmere Road , Dunmore, Elmshire<br>
        LP47 9XZ, UK
      </address>
      <span class="contact-rule"></span>
      <div class="contact-block">
        <div class="contact-line">
          <svg class="icon" viewBox="0 0 12 12"><path d="M2.5 1 4.5 3.3 3.4 4.6c.8 1.6 2.2 3 3.9 3.9L8.6 7.4 11 9.4 9.8 11C5.1 10.6 1.3 6.8 1 2.2z"/></svg>
          <span>+44 (0)1632 960418</span>
        </div>
        <div class="contact-line">
          <svg class="icon" viewBox="0 0 12 12"><rect x="1" y="3" width="3" height="8"/><rect x="5" y="3" width="6" height="8"/><rect x="6" y="1" width="4" height="2"/></svg>
          <span>+44 (0)1632 960733</span>
        </div>
      </div>
      <span class="contact-rule"></span>
      <div class="contact-block">
        <div class="contact-line">
          <svg class="icon" viewBox="0 0 12 12"><path d="M0 2h12v8H0zM1 3l5 4 5-4v-.2H1z" fill-rule="evenodd"/></svg>
          <span>sales@ktfabrications.example</span>
        </div>
        <div class="contact-line">
          <svg class="icon" viewBox="0 0 12 12"><circle cx="6" cy="6" r="5.5"/><path d="M.5 6h11M6 .5v11M2 3h8M2 9h8" stroke="#fff" stroke-width=".8"/></svg>
          <span>www.ktfabrications.example</span>
        </div>
      </div>
    </footer>
  </section>

  <section class="sheet comp-slip" aria-label="Compliments slip">
    <div class="brand-name">KT FABRICATIONS</div>
    <h1 class="slip-title">With Compliments</h1>

    <footer class="contact-footer">
      <address class="contact-block contact-address">
        KT Fabrications Limited<br>
        Hallmere Road , Dunmore, Elmshire<br>
        LP47 9XZ, UK
      </address>
      <span class="contact-rule"></span>
      <div class="contact-block">
        <div class="contact-line">
          <svg class="icon" viewBox="0 0 12 12"><path d="M2.5 1 4.5 3.3 3.4 4.6c.8 1.6 2.2 3 3.9 3.9L8.6 7.4 11 9.4 9.8 11C5.1 10.6 1.3 6.8 1 2.2z"/></svg>
          <span>+44 (0)1632 960418</span>
        </div>
        <div class="contact-line">
          <svg class="icon" viewBox="0 0 12 12"><rect x="1" y="3" width="3" height="8"/><rect x="5" y="3" width="6" height="8"/><rect x="6" y="1" width="4" height="2"/></svg>
          <span>+44 (0)1632 960733</span>
        </div>
      </div>
      <span class="contact-rule"></span>
      <div class="contact-block">
        <div class="contact-line">
          <svg class="icon" viewBox="0 0 12 12"><path d="M0 2h12v8H0zM1 3l5 4 5-4v-.2H1z" fill-rule="evenodd"/></svg>
          <span>sales@ktfabrications.example</span>
        </div>
        <div class="contact-line">
          <svg class="icon" viewBox="0 0 12 12"><circle cx="6" cy="6" r="5.5"/><path d="M.5 6h11M6 .5v11M2 3h8M2 9h8" stroke="#fff" stroke-width=".8"/></svg>
          <span>www.ktfabrications.example</span>
        </div>
      </div>
    </footer>
  </section>

</div>
</body>
</html>
```